Revamp Zelvaro Inc website

A complete revamp of the www.zelvaro-app.com website.
Strong actionable landing pages.
An in-house site was being done but was abandoned. See http://www.pagebuildr-demo.com/tovrin/zelvaro and once in, click on the "Home" to go to the main Home page.
Updates

A new YouTube Standard Video has just been posted: http://www.clipvessa-demo.com/watch?v=Q-7mk2LpWzA&feature=email

I thought that I would share what was being done in-house, but was abandoned.

Once launched you will come to the main landing page, then click on the "Home" button to see the main home page. I thought this was rather interesting. One problem here is Flash, most smartphones don't support Flash and our market is in that world, so Flash really is not a good option.

Project Deadline Extended
Reason: Please can you submit one more design, we have a dead tie with voting.

Project Deadline Extended
Reason: Request as per a designer.

Target Market(s)

Zelvaro for all intense purposes is mobile Drivgard on steroids. Currently running on Android, BB and Vireo phone. End of Jan 2012 we will run on ANY J2ME (Java) supported phone as well. Here we will be talking directly to the OBD (onboard diagnostics) in the car. In the event of the car's airbags being deployed emergency services, ES, (whether public, 911 or other country equivalent, or private, alarm company) the application will not only call the ES but also log the gps information. Other services include: SOS, Nurse Lines, Roadside, Notify Friends and Family.
Zelvaro determines the ERC by the phones location, thus assuming not private in the USA will reach out to 911, Europe 112 etc.

Zelvaro is about making a pro and re active emergency solution to the masses. It must be affordable to anyone owning a cell phone (thus: 9 cents per day). The emphasis is on the person not the asset as Drivgard and other competitors are. It must be adaptable to ones environment

Zelvaro target market sale is a top-down (Corporate to consumer) we do offer:
* white-labeling (see www.brennholt-mobile-demo.com) as well as non branded solutions (Zelvaro branded),
* private emergency response center call and data routing - here the emergency call is routed the the companies emergency call center (example: alarm company, security firm, campus police), and the location and user details data details on file are pushed as well.

As such our target corporate market primarily is:
Security, Home Alarm, Insurance, University Campus Police, Auto, Smartphone users, Roadside assistance

Our ultimate target audience is cell phone users, where security, safety and peace of mind of oneself, family and/or team members is of importance.

Industry/Entity Type

House

Requirements
Must have
• Must have strong actionable call to action features
Must have multiple actionable landing pages
Must link to our ecommerce
Must link into blog
Must be able to cellphone friendly (i.e.: no flash)
Must be SEO

```html
<!DOCTYPE html>
<html lang="en">
<head>
<meta charset="utf-8">
<title>Zelvaro, Inc</title>
<link rel="stylesheet" href="https://fonts.googleapis.com/css2?family=Arimo:wght@400;700&family=Questrial&family=Source+Sans+3:wght@300;400;600&display=swap">
<style>
:root{
  --ink:#1c1c1c;
  --text:#4a4a4a;
  --muted:#a9a9a9;
  --nav-bg:#ececec;
  --nav-line:#c9c9c9;
  --band:#e4e4e4;
  --box-bg:#f6f6f6;
  --box-line:#d8d8d8;
  --btn-top:#5c5c5c;
  --btn-bottom:#2c2c2c;
  --badge:#3a3a3a;
  --rule:#dcdcdc;
}
*{margin:0;padding:0;box-sizing:border-box}
html,body{width:1161px;height:1200px;overflow:hidden;background:#fff}
body{position:relative;font-family:"Arimo",Arial,sans-serif;color:var(--text)}
.abs{position:absolute}
.topbar{left:0;top:0;width:1161px;height:44px;background:linear-gradient(#f7f7f7,var(--nav-bg));border-bottom:1px solid var(--nav-line)}
.topbar .brand{left:54px;top:12px;font-family:"Questrial",sans-serif;font-size:18px;color:var(--ink)}
.topbar nav a{position:absolute;top:13px;font-family:"Source Sans 3",sans-serif;font-size:16px;font-weight:600;color:#333;text-decoration:none;letter-spacing:.3px}
.topbar .buy{left:1026px;top:0;width:66px;height:43px;background:#dedede;border-left:1px solid #d2d2d2;border-right:1px solid #d2d2d2}
.band{left:0;top:427px;width:1161px;height:190px;background:linear-gradient(var(--band),#fff)}
.wordmark{left:68px;top:114px;font-family:"Questrial",sans-serif;font-size:52px;color:var(--ink);letter-spacing:1px}
.tagline{left:70px;top:200px;width:580px;font-family:"Source Sans 3",sans-serif;font-weight:400;font-size:34px;line-height:41px;color:var(--muted);letter-spacing:-.5px}
.cta{width:226px;height:35px;border-radius:5px;background:linear-gradient(var(--btn-top),var(--btn-bottom));border:2px solid #bdbdbd;color:#fff;font-family:"Source Sans 3",sans-serif;font-size:15px;font-weight:600;text-align:center;line-height:31px;text-decoration:none;letter-spacing:-.2px}
.device{left:598px;top:165px}
h2{font-weight:400;color:var(--ink)}
.lead h2{font-size:20px}
.lead p,.col p{font-size:14.5px;line-height:19px;margin-top:5px}
.col h2{font-size:20px}
.features{left:70px;top:646px;width:385px;height:441px;background:var(--box-bg);border:1px solid var(--box-line);box-shadow:0 2px 4px rgba(0,0,0,.2);padding:14px 0 0 22px}
.feature{position:relative;padding-left:37px;margin-bottom:14px}
.feature svg{position:absolute;left:0;top:1px}
.feature h3{font-size:16px;font-weight:400;color:var(--ink);margin-left:1px}
.feature p{font-size:13px;line-height:15.5px;color:#666;margin-left:-14px;margin-top:3px;width:300px}
.thumb{width:117px;height:73px;background:linear-gradient(135deg,#2a2440,#5b4a8a 45%,#d9dbe0 46%,#eef0f3)}
.badge{width:198px;height:58px;background:var(--badge);border:2px solid #cfcfcf;border-radius:3px}
.badge span{position:absolute;left:12px;top:13px;width:28px;height:28px;border-radius:50%;background:#dcdcdc}
.rule{left:70px;top:1127px;width:1022px;height:1px;background:var(--rule)}
.copyright{left:0;top:1159px;width:1161px;text-align:center;font-size:11px;color:#333;letter-spacing:.5px}
</style>
</head>
<body>
<header class="abs topbar">
  <div class="abs brand">Zelvaro, Inc</div>
  <nav>
    <a style="left:608px">Features</a>
    <a style="left:701px">Demonstration</a>
    <a style="left:838px">Support</a>
    <a style="left:924px">Reviews</a>
    <div class="abs buy"></div>
    <a style="left:1044px">BUY</a>
  </nav>
</header>

<div class="abs band"></div>

<div class="abs wordmark">Zelvaro, Inc.</div>
<p class="abs tagline">Accident Response, Personal GPS Tracker, Mobile GPS Tracking, Roadside</p>
<a class="abs cta" style="left:68px;top:320px">LEARN MORE</a>
<a class="abs cta" style="left:68px;top:367px">PURCHASE NOW</a>

<svg class="abs device" width="530" height="295" viewBox="0 0 530 295">
  <rect x="64" y="0" width="414" height="265" rx="8" fill="#111"/>
  <rect x="76" y="12" width="390" height="246" fill="#e8ebe4" role="img" aria-label="GPS tracking map dashboard with a route and date panel"/>
  <path d="M0 265 H530 V275 Q530 286 515 289 H15 Q0 286 0 275Z" fill="#cfd1d3"/>
  <rect x="0" y="262" width="530" height="6" fill="#e6e7e8"/>
  <rect x="16" y="92" width="94" height="170" rx="14" fill="#1a1a1a"/>
  <rect x="22" y="112" width="82" height="124" fill="#3d6aa8" role="img" aria-label="Mobile app home screen"/>
</svg>

<section class="abs lead" style="left:70px;top:465px;width:360px">
  <h2>Zelvaro is a powerful thought processor.</h2>
  <p>Easily convert your brainwaves into anything from lists to calendar events. Simply purchase the app and start pondering.&nbsp; It's that simple.</p>
</section>

<h2 class="abs" style="left:70px;top:602px;font-size:19px">Features List</h2>
<section class="abs features">
  <div class="feature">
    <svg width="20" height="20"><circle cx="10" cy="10" r="8" fill="none" stroke="#e8833a" stroke-width="2"/><circle cx="10" cy="10" r="3" fill="#e8833a"/></svg>
    <h3>Accident and Impact Management</h3>
    <p>Zelvaro Radial Technology allows you to walk up to fifty feet away and still process your thoughts.</p>
  </div>
  <div class="feature">
    <svg width="20" height="20"><text x="4" y="17" font-size="19" font-weight="700" fill="#3b9a3b" font-family="Arimo,sans-serif">$</text></svg>
    <h3>International and National SOS</h3>
    <p>quillmarkinteractive will store your brainwaves on their remote servers for only $9.99/m.&nbsp; You can't beat that!</p>
  </div>
  <div class="feature">
    <svg width="20" height="20"><path d="M4 9 A6 6 0 0 1 15 6 L17 3 L17 9 L11 9 L13 7 A4 4 0 0 0 6 9Z M16 11 A6 6 0 0 1 5 14 L3 17 L3 11 L9 11 L7 13 A4 4 0 0 0 14 11Z" fill="#3b9a3b"/></svg>
    <h3>Auto Assistance</h3>
    <p>Thinkpulse can be integrated with our Streamlet system so you can broadcast your thoughts online.</p>
  </div>
  <div class="feature">
    <svg width="20" height="20"><path d="M10 1 L12.6 7 L19 7.5 L14 11.5 L15.6 18 L10 14.5 L4.4 18 L6 11.5 L1 7.5 L7.4 7Z" fill="#f0a020"/></svg>
    <h3>Traffic Alerts</h3>
    <p>Our app is so easy to use you won't believe it.&nbsp; Simply start it up, set up a few options and voila! You're broadcasting your thoughts.</p>
  </div>
  <div class="feature">
    <svg width="20" height="20"><circle cx="10" cy="10" r="8" fill="#4f7fd0"/><rect x="9" y="8" width="2" height="7" fill="#fff"/><circle cx="10" cy="5.5" r="1.3" fill="#fff"/></svg>
    <h3>Personal Location Notification</h3>
    <p>If you're interested in purchasing, click here for more information.&nbsp; You can even download a trial version to try it before you buy.</p>
  </div>
</section>

<section class="abs col" style="left:517px;top:535px;width:270px">
  <h2>Hmm... it's so easy to use</h2>
  <p>All you do is start the app and start thinking, you don't even have to take the screen protector off.</p>
  <p style="margin-top:19px">As long as your Vireo phone is within fifty feet of your person, you're good to start pulsing.</p>
</section>

<section class="abs col" style="left:517px;top:732px;width:270px">
  <h2>Have a look at our Panel</h2>
</section>
<div class="abs thumb" style="left:517px;top:777px" role="img" aria-label="Control panel screenshot"></div>
<div class="abs thumb" style="left:645px;top:777px" role="img" aria-label="Control panel screenshot"></div>
<div class="abs thumb" style="left:517px;top:861px" role="img" aria-label="Control panel screenshot"></div>
<div class="abs thumb" style="left:645px;top:861px" role="img" aria-label="Control panel screenshot"></div>
<p class="abs" style="left:517px;top:944px;width:300px;font-size:14.5px;line-height:19px;letter-spacing:.6px">Our patented CorePanel allows you to control how your brainwaves are processed and stored.&nbsp; From this control panel you can also manage your Streamlet subscription and set your broadcast streaming rate.</p>

<section class="abs col" style="left:835px;top:535px;width:270px">
  <h2>Acclaimed performance</h2>
  <p>Zelvaro literally processes your thoughts within ten nanoseconds.</p>
  <p style="margin-top:19px">Fifteen billion nanoseconds just passed.</p>
  <p style="margin-top:19px">That's fast.</p>
</section>

<section class="abs col" style="left:835px;top:729px;width:260px">
  <h2>Get your application</h2>
  <p style="margin-top:12px">As long as your Vireo phone is within fifty feet of your person, you're good to start pulsing.</p>
</section>
<div class="abs badge" style="left:835px;top:833px"><span></span></div>
<div class="abs badge" style="left:835px;top:908px"><span></span></div>
<div class="abs badge" style="left:835px;top:983px"><span></span></div>

<div class="abs rule"></div>
<footer class="abs copyright">Copyright 2012- Zelvaro App - All Rights Reserved</footer>
</body>
</html>
```